innovative investment real estate sales firm

We are a uniquely collabrative firm that seeks to bring a conultative approach to uncovering hidden opportunities for our clients, our website needs to convey our client focused approach. Our firm specializes in the sale of apartment properties in Southern California. We have a team of researchers, transaction coordinators and marketing personal to support our geographically specialized advisers. We need a website that introduces clients to our unique way of better helping them achieve their investment goals.

Target Market(s)

High net worth individuals and families

Industry/Entity Type

Real Estate Agent

Font styles to use
Other font styles liked:
• please use font provided

Requirements
Must have
• Stories of our recent projects
• Features on our people
• email capture for viewing inventory
• content that showcases our unique consultative approach that uncovers unrealized opportunities

```html
<!DOCTYPE html>
<html lang="en">
<head>
<meta charset="utf-8">
<title>Meridian Crest Advisors</title>
<link href="https://fonts.googleapis.com/css2?family=Quicksand:wght@500;700&family=Open+Sans:wght@400;600;700&display=swap" rel="stylesheet">
<style>
:root{
  --teal:#1ba3bb;
  --teal-deep:#168fa5;
  --green:#8dc21f;
  --green-dark:#76a716;
  --night:#16232a;
  --night-2:#1d2b31;
  --slate:#2c3038;
  --ink:#2a2a2a;
  --white:#ffffff;
  --muted:#8f9aa0;
  --line:#5c6a70;
}
*{margin:0;padding:0;box-sizing:border-box}
html,body{width:1200px;height:3750px;overflow:hidden}
body{position:relative;font-family:"Open Sans",Arial,sans-serif;color:var(--white);background:var(--white)}
.abs{position:absolute}
.heading{font-family:"Quicksand","Trebuchet MS",sans-serif;font-weight:700;text-transform:uppercase}

/* hero */
.hero{left:0;top:0;width:1200px;height:725px;background:linear-gradient(180deg,#3a4450 0%,#2c343d 45%,#3b3a3c 80%,#4a3f3a 100%)}
.brand{left:85px;top:25px;display:flex;align-items:center;gap:16px}
.brand-mark{width:70px;height:70px;border:3px solid var(--white);flex:none}
.brand-name{font-family:"Quicksand",sans-serif;font-weight:700;font-size:30px;line-height:1.05;color:var(--white);text-transform:uppercase;letter-spacing:1px}
.brand-name span{display:block}
.nav{right:85px;top:56px;display:flex;gap:42px;font-size:16px;text-transform:uppercase}
.nav a{color:var(--white);text-decoration:none}
.nav a.active{color:var(--green)}
.hero-title{left:0;width:1200px;top:305px;text-align:center;font-size:56px}
.hero-sub{left:380px;width:440px;top:385px;text-align:center;font-size:16px;font-weight:600;line-height:1.6}
.slide-arrow{top:330px;width:36px;height:36px;border:2px solid rgba(255,255,255,.7)}
.slide-arrow svg{display:block}

/* welcome */
.welcome{left:0;top:725px;width:1200px;height:367px;background:linear-gradient(135deg,var(--teal) 0%,#1ea9c0 55%,var(--teal-deep) 100%)}
.welcome h1{left:0;width:1200px;top:60px;text-align:center;font-size:45px}
.welcome p{left:130px;width:940px;top:137px;text-align:center;font-size:14.5px;line-height:1.8}
.btn-white{left:517px;top:255px;width:165px;height:50px;background:var(--white);color:var(--teal);font-size:18px;font-weight:600;display:flex;align-items:center;justify-content:center;text-transform:uppercase}

/* services */
.services{left:0;top:1092px;width:1200px;height:253px;background:linear-gradient(180deg,#132026,#1b2a30)}
.service{top:55px;width:335px;height:148px;border:1px solid var(--line)}
.service.alt{border-color:var(--green)}
.service-icon{left:2px;top:35px;width:80px;height:80px;border-radius:50%;background:var(--white);display:flex;align-items:center;justify-content:center}
.service.alt .service-icon{background:var(--green)}
.service h3{left:90px;top:36px;font-size:17px;font-weight:600;white-space:nowrap}
.service p{left:90px;top:72px;width:230px;font-size:13.5px;line-height:1.4;color:var(--muted)}

/* gallery */
.gallery{left:0;top:1345px;width:1200px;height:525px;background:#30383f}
.tile{position:absolute}
.find-home{left:600px;top:325px;width:300px;height:200px;background:var(--green);color:var(--ink);text-align:center}
.find-home h2{margin-top:48px;font-size:25px;color:var(--ink)}
.find-home p{margin:10px auto 0;width:240px;font-size:13.5px;line-height:1.4}
.btn-light{display:inline-flex;margin-top:12px;width:165px;height:40px;background:#f1f5e6;align-items:center;justify-content:center;font-size:16px;font-weight:600;text-transform:uppercase;color:var(--ink)}

/* properties */
.properties{left:0;top:1870px;width:1200px;height:537px;background:var(--white)}
.properties h2{left:0;width:1200px;top:48px;text-align:center;font-size:42px;color:var(--green)}
.card{top:125px;width:242px;height:350px;background:var(--white);box-shadow:0 2px 8px rgba(0,0,0,.18);border:1px solid #e3e3e3}
.card-photo{position:absolute;left:8px;top:8px;width:224px;height:190px}
.card h3{position:absolute;left:8px;top:205px;font-size:20px;color:var(--green);font-weight:700}
.card .price{position:absolute;left:8px;top:238px;font-size:17px;color:var(--ink);font-weight:600}
.card .meta{position:absolute;left:8px;top:270px;font-size:11px;color:#aaa;letter-spacing:.5px}
.card .btn-green{position:absolute;left:8px;top:295px;width:224px;height:42px;background:var(--green);display:flex;align-items:center;justify-content:center;color:var(--ink);font-size:16px;text-transform:uppercase}
.carousel-btn{top:280px;width:46px;height:46px;border-radius:50%;background:#f1f1f1;display:flex;align-items:center;justify-content:center}

/* team */
.team{left:0;top:2407px;width:1200px;height:443px;background:linear-gradient(180deg,#34373f,#2a2d33)}
.team h2{left:0;width:1200px;top:50px;text-align:center;font-size:42px}
.member{top:120px;width:255px;height:260px}
.member-intro{background:var(--teal);text-align:center}
.member-intro h3{margin-top:100px;font-size:21px;font-weight:600}
.member-intro p{margin:10px auto 0;width:200px;font-size:13.5px;line-height:1.4}
.member-name{position:absolute;left:0;bottom:20px;width:100%;text-align:center;font-size:19px}

/* map */
.map{left:0;top:2850px;width:1200px;height:400px;background:linear-gradient(135deg,#eef0eb 0%,#e4e8e0 40%,#b9d4ee 70%,#a9c9ea 100%)}

/* contact */
.contact{left:0;top:3250px;width:1200px;height:437px;background:linear-gradient(180deg,#1b1e22,#23262b)}
.contact h2{left:0;width:1200px;top:47px;text-align:center;font-size:42px}
.world{left:25px;top:100px;width:475px;height:320px}
.phone-box{left:212px;top:182px;width:300px;height:143px;background:rgba(0,0,0,.55)}
.phone{position:absolute;left:20px;top:35px;display:flex;align-items:center;gap:10px;font-size:22px;color:var(--green);white-space:nowrap}
.socials{position:absolute;left:50px;top:85px;display:flex;gap:16px}
.socials span{width:34px;height:34px;border-radius:50%;border:1px solid #666}
.socials span.on{background:var(--green);border-color:var(--green)}
.field{left:685px;width:437px;height:50px;background:var(--white);color:#aaa;font-size:14px;padding:14px 12px}
.field.msg{height:80px}
.submit{left:685px;top:332px;width:437px;height:50px;background:var(--green);color:var(--ink);display:flex;align-items:center;justify-content:center;font-size:16px;text-transform:uppercase}

/* footer */
.footer{left:0;top:3687px;width:1200px;height:63px;background:var(--green);color:var(--ink);display:flex;align-items:center;justify-content:center;font-size:14px;gap:6px}
.footer strong{font-family:"Quicksand",sans-serif;font-size:19px}
</style>
</head>
<body>

<header class="hero abs" role="img" aria-label="City skyline of tall glass towers at dusk">
  <div class="brand abs"><span class="brand-mark"></span><span class="brand-name"><span>Meridian Crest</span><span>Advisors</span></span></div>
  <nav class="nav abs">
    <a class="active" href="#">Home</a><a href="#">About Us</a><a href="#">Recent Project</a><a href="#">Contact Us</a>
  </nav>
  <div class="slide-arrow abs" style="left:45px"><svg width="32" height="32" viewBox="0 0 32 32"><path d="M19 9l-7 7 7 7" fill="none" stroke="#fff" stroke-width="2.5"/></svg></div>
  <div class="slide-arrow abs" style="left:1118px"><svg width="32" height="32" viewBox="0 0 32 32"><path d="M13 9l7 7-7 7" fill="none" stroke="#fff" stroke-width="2.5"/></svg></div>
  <h1 class="hero-title heading abs">Find Your Dream Home</h1>
  <p class="hero-sub abs">Lorem Ipsum is simply dummy text of the printing and typesetting industry Lorem Ipsum has.</p>
</header>

<section class="welcome abs">
  <h1 class="heading abs">Welcome to Meridian Crest Advisors</h1>
  <p class="abs">Lorem Ipsum is simply dummy text of the printing and typesetting industry. Lorem Ipsum has been the industry's standard dummy text ever since the 1500s, when an unknown printer took a galley of type and scrambled it to make a type specimen book. It has survived not only five centuries, but also the leap into electronic typesetting, remaining essentially unchanged. It was popularised in the 1960s with the release of Letraset sheets containing Lorem Ipsum passages, and more recently with desktop publishing software.</p>
  <div class="btn-white abs">Read More</div>
</section>

<section class="services abs">
  <div class="service abs" style="left:75px">
    <div class="service-icon abs"><svg width="44" height="44" viewBox="0 0 44 44" fill="none" stroke="#222" stroke-width="2.5"><circle cx="22" cy="19" r="9"/><path d="M18 29h8M19 34h6M22 4v3M8 19h3M33 19h3M12 9l2 2M32 9l-2 2"/></svg></div>
    <h3 class="abs">Researchers</h3>
    <p class="abs">Lorem Ipsum is simply dummy text of the printing and typesetting</p>
  </div>
  <div class="service alt abs" style="left:470px">
    <div class="service-icon abs"><svg width="44" height="44" viewBox="0 0 44 44" fill="none" stroke="#222" stroke-width="2.5"><rect x="8" y="10" width="22" height="26"/><path d="M14 18h10M14 24h8M22 32l14-16 3 3-14 16-4 1z"/></svg></div>
    <h3 class="abs">Transaction coordinators</h3>
    <p class="abs">Lorem Ipsum is simply dummy text of the printing and typesetting</p>
  </div>
  <div class="service abs" style="left:827px">
    <div class="service-icon abs"><svg width="44" height="44" viewBox="0 0 44 44" fill="none" stroke="#222" stroke-width="2.5"><circle cx="22" cy="22" r="15"/><path d="M7 22h30M22 7c-6 8-6 22 0 30M22 7c6 8 6 22 0 30"/></svg></div>
    <h3 class="abs">Support our geographically</h3>
    <p class="abs">Lorem Ipsum is simply dummy text of the printing and typesetting</p>
  </div>
</section>

<section class="gallery abs">
  <div class="tile" style="left:0;top:0;width:300px;height:210px;background:linear-gradient(135deg,#7d8f9e,#5a6a72)" role="img" aria-label="Rooftop pool terrace with lounge chairs"></div>
  <div class="tile" style="left:0;top:210px;width:300px;height:315px;background:linear-gradient(180deg,#3f5466,#2a3a44)" role="img" aria-label="Modern apartment block with balconies"></div>
  <div class="tile" style="left:300px;top:0;width:300px;height:347px;background:linear-gradient(160deg,#5b6670,#2f363d)" role="img" aria-label="Glass tower seen from below"></div>
  <div class="tile" style="left:300px;top:347px;width:300px;height:178px;background:linear-gradient(180deg,#6a7a6a,#3f5a3c)" role="img" aria-label="Residential tower among green trees"></div>
  <div class="tile" style="left:600px;top:0;width:300px;height:180px;background:linear-gradient(180deg,#4a4038,#2a2e36)" role="img" aria-label="Lit pool courtyard at night"></div>
  <div class="tile" style="left:600px;top:180px;width:300px;height:145px;background:linear-gradient(180deg,#5c7890,#3a4a56)" role="img" aria-label="City skyline by the water"></div>
  <div class="tile" style="left:900px;top:0;width:300px;height:325px;background:linear-gradient(160deg,#6b8088,#37474e)" role="img" aria-label="High-rise apartment building"></div>
  <div class="tile" style="left:900px;top:325px;width:300px;height:200px;background:linear-gradient(180deg,#4e5d68,#2e3940)" role="img" aria-label="Apartment building exterior"></div>
  <div class="tile find-home">
    <h2 class="heading">Find a Home</h2>
    <p>Lorem Ipsum is simply dummy text of the printing and typesetting.</p>
    <span class="btn-light">Read More</span>
  </div>
</section>

<section class="properties abs">
  <h2 class="heading abs">Available Properties</h2>
  <div class="carousel-btn abs" style="left:8px"><svg width="16" height="16" viewBox="0 0 16 16"><path d="M10 3L5 8l5 5" fill="none" stroke="#222" stroke-width="2"/></svg></div>
  <div class="carousel-btn abs" style="left:1146px"><svg width="16" height="16" viewBox="0 0 16 16"><path d="M6 3l5 5-5 5" fill="none" stroke="#8dc21f" stroke-width="2"/></svg></div>
  <article class="card abs" style="left:82px">
    <div class="card-photo" style="background:linear-gradient(180deg,#3a3050,#c07a3a)" role="img" aria-label="Luxury home with pool at dusk"></div>
    <h3 class="heading">Property Name</h3><div class="price">PRICE : $154,192.00</div><div class="meta">3 BEDS &nbsp;/&nbsp; 2 BATHS</div><div class="btn-green">View Details</div>
  </article>
  <article class="card abs" style="left:347px">
    <div class="card-photo" style="background:linear-gradient(180deg,#d98a4a,#6a5a70)" role="img" aria-label="Row of painted townhouses before a city skyline"></div>
    <h3 class="heading">Property Name</h3><div class="price">PRICE : $154,192.00</div><div class="meta">3 BEDS &nbsp;/&nbsp; 2 BATHS</div><div class="btn-green">View Details</div>
  </article>
  <article class="card abs" style="left:612px">
    <div class="card-photo" style="background:linear-gradient(180deg,#4a8ed0,#8fa0a8)" role="img" aria-label="Modern apartment building under blue sky"></div>
    <h3 class="heading">Property Name</h3><div class="price">PRICE : $154,192.00</div><div class="meta">3 BEDS &nbsp;/&nbsp; 2 BATHS</div><div class="btn-green">View Details</div>
  </article>
  <article class="card abs" style="left:877px">
    <div class="card-photo" style="background:linear-gradient(180deg,#6aa0d8,#b0a898)" role="img" aria-label="Contemporary multifamily building"></div>
    <h3 class="heading">Property Name</h3><div class="price">PRICE : $154,192.00</div><div class="meta">3 BEDS &nbsp;/&nbsp; 2 BATHS</div><div class="btn-green">View Details</div>
  </article>
</section>

<section class="team abs">
  <h2 class="heading abs">Our Team</h2>
  <div class="member member-intro abs" style="left:90px">
    <h3>Lorem ipsum dummy</h3>
    <p>We know that real transformation happens when your people are invested</p>
    <svg width="20" height="16" viewBox="0 0 20 16" style="margin-top:4px"><path d="M4 3l6 5 6-5M4 9l6 5 6-5" fill="none" stroke="#fff" stroke-width="2"/></svg>
  </div>
  <div class="member abs" style="left:345px;background:linear-gradient(180deg,#5a6a5e,#2e3a34)" role="img" aria-label="Portrait of a team member"><span class="member-name">Lorem Ipsum</span></div>
  <div class="member abs" style="left:600px;background:linear-gradient(180deg,#6e6a66,#3a3634)" role="img" aria-label="Portrait of a team member"><span class="member-name">Lorem Ipsum</span></div>
  <div class="member abs" style="left:855px;background:linear-gradient(180deg,#4f6a4a,#2e3e2c)" role="img" aria-label="Portrait of a team member"><span class="member-name">Lorem Ipsum</span></div>
</section>

<section class="map abs" role="img" aria-label="Street map of the office area with a location pin"></section>

<section class="contact abs">
  <h2 class="heading abs">Contact Us</h2>
  <div class="world abs" role="img" aria-label="Dotted world map" style="background:radial-gradient(ellipse at 50% 50%,rgba(200,200,200,.18),rgba(0,0,0,0) 70%)"></div>
  <div class="phone-box abs">
    <div class="phone"><svg width="26" height="26" viewBox="0 0 24 24" fill="none" stroke="#fff" stroke-width="1.8"><path d="M5 3h4l2 5-2.5 1.5a11 11 0 006 6L16 13l5 2v4a2 2 0 01-2 2A17 17 0 013 5a2 2 0 012-2z"/></svg>+44 (0) 7000 000123</div>
    <div class="socials"><span class="on"></span><span></span><span></span><span></span></div>
  </div>
  <div class="field abs" style="top:125px">Name</div>
  <div class="field abs" style="top:182px">E-Mail Address</div>
  <div class="field msg abs" style="top:240px">Message</div>
  <div class="submit abs">Submit</div>
</section>

<footer class="footer abs">© <strong>Meridian Crest Advisors</strong> - 2017 All Right Reserved</footer>

</body>
</html>
```